Doggy Shampoo needs a shout-out Sticker design for its bottle

We need a front-and-back sticker design for our 500ml doggy shampoo bottle (bottle design attached). Bottle color has not been determined yet, but it will not be a clear bottle. Most likely white or other bright colors. This shampoo contains virgin coconut oil (VCO) and fruit extract for soft and shiny fur, and the formula is paraben-free for the health conscious. We want our bottle to stand out among others on store shelves.

Target Market(s)

Target buyers are social media conscious dog owners who cares about the appearance, happiness and health of their pets.

Industry/Entity Type

Pet Care

Colors

Designer to choose colors to be used in the design.

Requirements
Must have
• Logo/Brand as attached.
• Must mention that it contains Virgin Coconut Oil (VCO) and fruit extract for soft and shiny fur (wordings for the benefit can be modified).
• In the back sticker design, for ingredients, just put any 5 or 6 usual ingredients because it will probably be edited again and save space for barcode and QR Code.
Nice to have
• The cutout shape of the sticker is as enclosed.
Should not have
• We would prefer not to have photograph of a dog in the design because photographs are in most of pet products and our bottle will not stand out. Instead, you can provide a nice, fashionable or groovy drawing of a dog or dogs.

```html
<!DOCTYPE html>
<html lang="en">
<head>
<meta charset="utf-8">
<title>Pawlo Doggy Shampoo – Front Label Options</title>
<link rel="stylesheet" href="https://fonts.googleapis.com/css2?family=Libre+Baskerville:wght@400&family=Montserrat:wght@700&family=Open+Sans:wght@400;700&family=Questrial&display=swap">
<style>
  :root{
    --bg-red:#e8393a;
    --white:#ffffff;
    --green-top:#b6de74;
    --green-bottom:#6ae878;
    --green-ring-light:#9fd27a;
    --green-ring-dark:#6ea85e;
    --blue-top:#cfe0e5;
    --blue-bottom:#8fc3d9;
    --blue-ring:#17a3cc;
    --art-yellow:#fec43a;
    --ink:#1f1f1f;
    --badge-dark:#2b2b2b;
  }
  *{box-sizing:border-box;margin:0;padding:0}
  html,body{width:1200px;height:886px;overflow:hidden}
  body{background:var(--bg-red);position:relative;font-family:"Open Sans",sans-serif;color:var(--ink)}
  .sheet-title{position:absolute;top:48px;left:0;width:1200px;text-align:center;
    font-family:"Questrial",sans-serif;font-size:46px;font-weight:400;color:var(--white);letter-spacing:1px}
  .option{position:absolute;top:144px;width:338px;height:588px}
  .option--one{left:70px}.option--two{left:432px}.option--three{left:794px}
  .option-caption{position:absolute;top:616px;left:0;width:338px;text-align:center;
    font-family:"Questrial",sans-serif;font-size:34px;color:var(--white)}
  .label-shape{position:absolute;inset:0;width:338px;height:588px}
  .brand{position:absolute;top:52px;left:0;width:338px;text-align:center;
    font-family:"Open Sans",sans-serif;font-weight:700;font-size:54px;line-height:1;color:var(--white)}
  .product-name{position:absolute;top:426px;left:0;width:338px;text-align:center;
    font-family:"Libre Baskerville",serif;font-size:25px;letter-spacing:1px;color:var(--ink)}
  .option--two .product-name{font-family:"Montserrat",sans-serif;font-weight:700;font-size:26px;top:424px}
  .claims{position:absolute;top:470px;left:0;width:338px;height:80px}
  .claim{position:absolute;text-align:center;font-size:15px;line-height:16px;transform:translateX(-50%)}
  .claim--paw{top:0}
  .claim--paw svg{display:block;margin:0 auto 4px}
  .claim--disc{top:-4px;width:84px;height:84px;border-radius:50%;background:var(--badge-dark);
    border:2px solid #111;box-shadow:0 0 0 2px #777 inset;color:var(--white);
    display:flex;align-items:center;justify-content:center}
  .claim--wreath{top:2px;width:72px;height:74px;display:flex;align-items:center;justify-content:center;white-space:nowrap}
  .claim--wreath .wreath{position:absolute;left:0;top:0;width:100%;height:100%;overflow:visible}
  .claim--wreath span{position:relative}
  .volume{position:absolute;top:556px;left:0;width:338px;text-align:center;font-weight:700;font-size:16px;letter-spacing:1px}
</style>
</head>
<body>
  <h1 class="sheet-title">FRONT</h1>

  <!-- Option 1 -->
  <section class="option option--one">
    <svg class="label-shape" viewBox="0 0 338 588">
      <defs>
        <linearGradient id="greenFill" x1="0" y1="0" x2="0" y2="1">
          <stop offset="0.8" stop-color="var(--green-top)"/><stop offset="1" stop-color="var(--green-bottom)"/>
        </linearGradient>
        <linearGradient id="greenRing" x1="0" y1="0" x2="0" y2="1">
          <stop offset="0" stop-color="var(--green-ring-light)"/><stop offset="1" stop-color="var(--green-ring-dark)"/>
        </linearGradient>
      </defs>
      <path d="M0,110 Q0,78 30,64 L150,8 Q169,-1 188,8 L308,64 Q338,78 338,110 L338,548 Q338,588 298,588 L40,588 Q0,588 0,548 Z" fill="url(#greenFill)"/>
      <line x1="28" y1="166" x2="310" y2="166" stroke="#8fbf64" stroke-width="2" opacity=".6"/>
      <path d="M100,166 Q100,142 126,142 L212,142 Q238,142 238,166 L238,200 L100,200 Z" fill="#a8d88a"/>
      <circle cx="169" cy="296" r="117" fill="url(#greenRing)"/>
      <rect x="126" y="150" width="86" height="70" fill="#a8d88a"/>
      <circle cx="169" cy="296" r="95" fill="var(--art-yellow)" role="img" aria-label="Illustration of a winking grey bulldog wearing a red polka-dot bandana"/>
    </svg>
    <div class="brand">Pawlo</div>
    <div class="product-name">DOGGY SHAMPOO</div>
    <div class="claims">
      <div class="claim claim--paw" style="left:56px"><svg width="34" height="30" viewBox="0 0 34 30"><ellipse cx="17" cy="21" rx="9" ry="8" fill="#222"/><ellipse cx="5" cy="12" rx="4" ry="5" fill="#222"/><ellipse cx="12" cy="5" rx="4" ry="5" fill="#222"/><ellipse cx="22" cy="5" rx="4" ry="5" fill="#222"/><ellipse cx="29" cy="12" rx="4" ry="5" fill="#222"/></svg>Fruit<br>Extract</div>
      <div class="claim claim--paw" style="left:168px;white-space:nowrap"><svg width="34" height="30" viewBox="0 0 34 30"><ellipse cx="17" cy="21" rx="9" ry="8" fill="#222"/><ellipse cx="5" cy="12" rx="4" ry="5" fill="#222"/><ellipse cx="12" cy="5" rx="4" ry="5" fill="#222"/><ellipse cx="22" cy="5" rx="4" ry="5" fill="#222"/><ellipse cx="29" cy="12" rx="4" ry="5" fill="#222"/></svg>Virgin Coconut<br>Oil (VCO)</div>
      <div class="claim claim--paw" style="left:280px"><svg width="34" height="30" viewBox="0 0 34 30"><ellipse cx="17" cy="21" rx="9" ry="8" fill="#222"/><ellipse cx="5" cy="12" rx="4" ry="5" fill="#222"/><ellipse cx="12" cy="5" rx="4" ry="5" fill="#222"/><ellipse cx="22" cy="5" rx="4" ry="5" fill="#222"/><ellipse cx="29" cy="12" rx="4" ry="5" fill="#222"/></svg>Paraben<br>Free</div>
    </div>
    <div class="volume">500ml</div>
    <div class="option-caption">Option 1</div>
  </section>

  <!-- Option 2 -->
  <section class="option option--two">
    <svg class="label-shape" viewBox="0 0 338 588">
      <defs>
        <linearGradient id="blueFill" x1="0" y1="0" x2="0" y2="1">
          <stop offset="0.35" stop-color="var(--blue-top)"/><stop offset="1" stop-color="var(--blue-bottom)"/>
        </linearGradient>
        <linearGradient id="blueRing" x1="0" y1="0" x2="0" y2="1">
          <stop offset="0" stop-color="#e2eef0"/><stop offset="0.6" stop-color="#a8d3e0"/><stop offset="1" stop-color="var(--blue-ring)"/>
        </linearGradient>
      </defs>
      <path d="M0,110 Q0,78 30,64 L150,8 Q169,-1 188,8 L308,64 Q338,78 338,110 L338,548 Q338,588 298,588 L40,588 Q0,588 0,548 Z" fill="url(#blueFill)"/>
      <line x1="28" y1="166" x2="310" y2="166" stroke="#9fbcc6" stroke-width="2" opacity=".6"/>
      <path d="M100,166 Q100,142 126,142 L212,142 Q238,142 238,166 L238,200 L100,200 Z" fill="#d8e7ea"/>
      <circle cx="169" cy="292" r="115" fill="url(#blueRing)"/>
      <rect x="126" y="150" width="86" height="70" fill="#dde9ec"/>
      <circle cx="169" cy="292" r="94" fill="var(--art-yellow)" role="img" aria-label="Illustration of a winking grey bulldog wearing a red polka-dot bandana"/>
    </svg>
    <div class="brand">Pawlo</div>
    <div class="product-name">DOGGY SHAMPOO</div>
    <div class="claims">
      <div class="claim claim--disc" style="left:70px">Fruit<br>Extract</div>
      <div class="claim claim--disc" style="left:169px">Virgin<br>Coconut<br>Oil</div>
      <div class="claim claim--disc" style="left:268px">Paraben<br>Free</div>
    </div>
    <div class="volume">500ml</div>
    <div class="option-caption">Option 2</div>
  </section>

  <!-- Option 3 -->
  <section class="option option--three">
    <svg class="label-shape" viewBox="0 0 338 588">
      <path d="M0,110 Q0,78 30,64 L150,8 Q169,-1 188,8 L308,64 Q338,78 338,110 L338,548 Q338,588 298,588 L40,588 Q0,588 0,548 Z" fill="url(#greenFill)"/>
      <line x1="28" y1="166" x2="310" y2="166" stroke="#8fbf64" stroke-width="2" opacity=".6"/>
      <path d="M100,166 Q100,142 126,142 L212,142 Q238,142 238,166 L238,200 L100,200 Z" fill="#a8d88a"/>
      <circle cx="169" cy="296" r="117" fill="url(#greenRing)"/>
      <rect x="126" y="150" width="86" height="70" fill="#a8d88a"/>
      <circle cx="169" cy="296" r="95" fill="var(--art-yellow)" role="img" aria-label="Illustration of a winking grey bulldog wearing a red polka-dot bandana"/>
    </svg>
    <div class="brand">Pawlo</div>
    <div class="product-name">DOGGY SHAMPOO</div>
    <div class="claims">
      <div class="claim claim--wreath" style="left:56px"><svg class="wreath" viewBox="0 0 72 74"><path d="M4,24 Q36,-2 68,24" fill="none" stroke="#222" stroke-width="3"/><path d="M4,50 Q36,76 68,50" fill="none" stroke="#222" stroke-width="3"/><polygon points="36,2 38.5,7 44,7 39.5,10.5 41,16 36,12.5 31,16 32.5,10.5 28,7 33.5,7" fill="#222"/><polygon points="36,58 38.5,63 44,63 39.5,66.5 41,72 36,68.5 31,72 32.5,66.5 28,63 33.5,63" fill="#222"/></svg><span>Fruit<br>Extract</span></div>
      <div class="claim claim--wreath" style="left:169px"><svg class="wreath" viewBox="0 0 72 74"><path d="M4,24 Q36,-2 68,24" fill="none" stroke="#222" stroke-width="3"/><path d="M4,50 Q36,76 68,50" fill="none" stroke="#222" stroke-width="3"/><polygon points="36,2 38.5,7 44,7 39.5,10.5 41,16 36,12.5 31,16 32.5,10.5 28,7 33.5,7" fill="#222"/><polygon points="36,58 38.5,63 44,63 39.5,66.5 41,72 36,68.5 31,72 32.5,66.5 28,63 33.5,63" fill="#222"/></svg><span>Virgin Coconut<br>Oil (VCO)</span></div>
      <div class="claim claim--wreath" style="left:277px"><svg class="wreath" viewBox="0 0 72 74"><path d="M4,24 Q36,-2 68,24" fill="none" stroke="#222" stroke-width="3"/><path d="M4,50 Q36,76 68,50" fill="none" stroke="#222" stroke-width="3"/><polygon points="36,2 38.5,7 44,7 39.5,10.5 41,16 36,12.5 31,16 32.5,10.5 28,7 33.5,7" fill="#222"/><polygon points="36,58 38.5,63 44,63 39.5,66.5 41,72 36,68.5 31,72 32.5,66.5 28,63 33.5,63" fill="#222"/></svg><span>Paraben<br>Free</span></div>
    </div>
    <div class="volume">500ml</div>
    <div class="option-caption">Option 3</div>
  </section>
</body>
</html>
```